Dinewell - Trifold Design Project

I have an example of what i am looking for. My company is a restaurant reservation and table management system. This tri-fold will be handed out to restaurant owners in a effort to get them to sign up. The tri-fold should be informative enough where it will make them interested and want to call me. I would like to highlight the low price of the system. I am uploading the tri-fold that i made in word so you have an idea of my system and have the content to add to your design.

you can also visit my website: www.dinewell-example.com

Please email me and let me know if you need anything further.
Updates

Target Market(s)

restaurant owners

Industry/Entity Type

Restaurant

Requirements
Must have
• clean and clear images and logo's. Must be created in Adobe illustrator or something comparable where i can send it to the printer.

I include the color scale for my logos.

```html
<!DOCTYPE html>
<html lang="en">
<head>
<meta charset="utf-8">
<title>Dinewell Trifold</title>
<link href="https://fonts.googleapis.com/css2?family=Raleway:wght@300;400;600&family=Open+Sans:wght@400;600&display=swap" rel="stylesheet">
<style>
  :root{
    --stage:#e8ebed;
    --white:#ffffff;
    --ink:#2a3a42;
    --accent:#2f86c2;
    --teal-deep:#1f3945;
    --teal-mid:#3f5f6c;
    --teal-soft:#7d97a2;
    --mist:#dfe6e9;
    --band:#e2e4e5;
    --photo-a:#c9d3da;
    --photo-b:#7e909c;
  }
  *{margin:0;padding:0;box-sizing:border-box}
  html,body{width:1200px;height:661px;overflow:hidden}
  body{background:var(--stage);font-family:"Open Sans",Arial,sans-serif;color:var(--ink)}
  .trifold{position:absolute;left:203px;top:20px;width:795px;height:621px;display:flex;box-shadow:0 2px 10px rgba(0,0,0,.15)}
  .panel{position:relative;width:265px;height:621px;overflow:hidden;background:var(--white)}

  /* Panel: offer */
  .offer-header{position:absolute;left:0;top:0;width:100%;height:105px;padding:34px 0 0 22px}
  .offer-title{font-family:"Raleway",Arial,sans-serif;font-weight:400;color:var(--accent);font-size:14px}
  .offer-intro{font-size:11.5px;line-height:1.35;margin-top:6px;width:200px}
  .offer-photo{position:absolute;left:0;top:105px;width:100%;height:300px;background:linear-gradient(160deg,var(--photo-a) 0%,#a8b6c0 45%,var(--photo-b) 100%)}
  .offer-base{position:absolute;left:0;top:405px;width:100%;height:216px;background:linear-gradient(180deg,#6f8894 0%,var(--teal-mid) 30%,var(--teal-deep) 100%)}
  .price-circle{position:absolute;left:-27px;top:228px;width:220px;height:220px;border-radius:50%;background:rgba(255,255,255,.35)}
  .price-points{position:absolute;left:20px;top:310px;color:var(--white);font-family:"Raleway",Arial,sans-serif;font-size:16px;line-height:1.25}
  .start-title{position:absolute;right:20px;top:450px;color:var(--white);font-family:"Raleway",Arial,sans-serif;font-size:13px;letter-spacing:.5px}
  .start-steps{position:absolute;left:20px;top:478px;width:230px;color:var(--white);font-size:8.5px;line-height:1.3;list-style:none}
  .start-steps li{display:flex;gap:8px;margin-bottom:9px}
  .fine-print{position:absolute;left:14px;bottom:10px;width:238px;color:rgba(255,255,255,.8);font-size:5.5px;line-height:1.35}

  /* Panel: contact */
  .contact{background:linear-gradient(180deg,var(--teal-deep) 0%,var(--teal-mid) 12%,var(--teal-soft) 25%,var(--mist) 42%,var(--white) 55%)}
  .company{position:absolute;left:0;top:428px;width:100%;text-align:center}
  .company-mark{display:block;width:36px;height:36px;margin:0 auto 6px;background:var(--teal-soft);border:2px solid var(--mist)}
  .company-name{font-size:12px;font-weight:600}
  .company-address{font-size:8.5px;line-height:1.35;margin-top:3px}
  .contact-band{position:absolute;left:0;top:545px;width:100%;height:76px;background:var(--band);padding:9px 0 0 80px}
  .contact-line{display:flex;align-items:center;gap:7px;font-size:8.5px;height:15px}
  .contact-line svg{width:11px;height:11px}

  /* Panel: cover */
  .cover-header{position:absolute;left:0;top:0;width:100%;height:105px;text-align:center;padding-top:35px}
  .cover-brand{font-family:"Raleway",Arial,sans-serif;font-weight:300;font-size:32px;color:var(--accent)}
  .cover-photo{position:absolute;left:0;top:105px;width:100%;height:292px;background:linear-gradient(200deg,#dfe6ea 0%,#a9bcc7 40%,#6e8592 100%)}
  .cover-base{position:absolute;left:0;top:397px;width:100%;height:224px;background:linear-gradient(180deg,#5c7885 0%,var(--teal-mid) 35%,var(--teal-deep) 100%)}
  .cover-title{position:absolute;right:22px;top:436px;color:var(--white);font-family:"Raleway",Arial,sans-serif;font-weight:300;font-size:36px}
  .cover-tagline{position:absolute;right:22px;top:488px;width:200px;text-align:right;color:var(--white);font-family:"Raleway",Arial,sans-serif;font-size:11.5px;line-height:1.3}
  .service-strip{position:absolute;left:0;bottom:0;width:100%;height:30px;background:rgba(0,0,0,.25);color:var(--white);font-size:8.5px;padding:9px 0 0 12px;word-spacing:1px}
</style>
</head>
<body>
<main class="trifold">

  <section class="panel offer">
    <header class="offer-header">
      <h2 class="offer-title">Complete Front of The House Solution</h2>
      <p class="offer-intro">Dinewell is the newest innovation in restaurant applications.</p>
    </header>
    <div class="offer-photo" role="img" aria-label="Close-up photo of a silver fork on a white table setting"></div>
    <div class="offer-base"></div>
    <div class="price-circle"></div>
    <p class="price-points">No Contract<br>$100 per month<br>NO additional cost*<br>60 day free trial!</p>
    <h3 class="start-title">HOW TO GET STARTED :</h3>
    <ol class="start-steps">
      <li><span>1.</span><span>Download the tablet Dinewell manager app from the app store, or scan the bar code on the next page.</span></li>
      <li><span>2.</span><span>Go to www.dinewell-example.com and sign up for an account</span></li>
      <li><span>3.</span><span>Enter the activation code on the tablet</span></li>
      <li><span>4.</span><span>That's it! You are ready to go</span></li>
    </ol>
    <p class="fine-print">* additional cost of $0.01 per text message sent with this paging system to diners without the smartphone app, no additional cost for customers who have downloaded the Dinewell app.</p>
  </section>

  <section class="panel contact">
    <div class="company">
      <span class="company-mark"></span>
      <p class="company-name">Dinewell, LLC</p>
      <p class="company-address">48 Harbor Lane, Suite 200<br>Easton, New York 10590</p>
    </div>
    <div class="contact-band">
      <p class="contact-line"><svg viewBox="0 0 12 12"><circle cx="6" cy="6" r="6" fill="#2a3a42"/><path d="M4 3.2l1 1.3-.6.8a4 4 0 0 0 2.3 2.3l.8-.6 1.3 1-.7.9C6 8.7 3.3 6 3.1 4z" fill="#fff"/></svg>555.014.2290</p>
      <p class="contact-line"><svg viewBox="0 0 12 12"><circle cx="6" cy="6" r="6" fill="#2a3a42"/><rect x="3" y="4" width="6" height="4.5" fill="#fff"/></svg>555.014.7731</p>
      <p class="contact-line"><svg viewBox="0 0 12 12"><circle cx="6" cy="6" r="6" fill="#2a3a42"/><rect x="3" y="4" width="6" height="4" fill="none" stroke="#fff"/><path d="M3 4l3 2.2L9 4" fill="none" stroke="#fff"/></svg>hello@dinewell-example.com</p>
      <p class="contact-line"><svg viewBox="0 0 12 12"><circle cx="6" cy="6" r="6" fill="#2a3a42"/><circle cx="6" cy="6" r="3" fill="none" stroke="#fff" stroke-width=".8"/><path d="M3 6h6M6 3v6" stroke="#fff" stroke-width=".6"/></svg>www.dinewell-example.com</p>
    </div>
  </section>

  <section class="panel cover">
    <header class="cover-header">
      <h1 class="cover-brand">Dinewell</h1>
    </header>
    <div class="cover-photo" role="img" aria-label="Photo of wine glasses on a waterfront table with a steel arch bridge behind"></div>
    <div class="cover-base"></div>
    <h2 class="cover-title">Dinewell</h2>
    <p class="cover-tagline">Offers The Most Advanced Method of Making Restaurant Reservations</p>
    <p class="service-strip">Reservations . Wait List . Table Management . Paging</p>
  </section>

</main>
</body>
</html>
```